Morvex Business Card (intended for Business Card sized magnet)

Hi guys,

I would like to get a design for my business card for the restaurant. The design must be single sided as I intend to produce business card sized magnets.

The File attached must me on and I'm open for new ides

Can you please ensure that the design meets Cardowell's magnetic business card size specifications:

http://www.cardowell.example.au/custom-magnets.aspx?txi=15695&xnid=TopNav_Magnetic+Business+Cards+(linked+item)_Magnets_Marketing+Products&xnav=TopNav

Full Bleed Size (starting document size):
90 x 52 mm
1062 x 615 pixels
* Finished artwork should use the full bleed dimensions for best results.

Document Trim Size (final size after being cut):
87 x 49 mm
1028 x 579 pixels
* Please be sure to keep all text within the safe margin.

Resolution:
300 DPI

The winning design/source files need to meet these specifications.

Thanks
Updates

Hi guys, can I see more options please Thanks

```html
<!DOCTYPE html>
<html lang="en">
<head>
<meta charset="utf-8">
<title>Morvex Business Card</title>
<link rel="stylesheet" href="https://fonts.googleapis.com/css2?family=Alegreya+Sans:wght@400;500&display=swap">
<style>
  :root {
    --page-bg: #f0efed;
    --card-base: #f7e2a6;
    --card-swirl: #e9cf8f;
    --card-light: #fbe9b8;
    --ink: #1f1d1a;
    --shadow: rgba(0, 0, 0, 0.18);
  }
  html, body {
    margin: 0;
    padding: 0;
    width: 1200px;
    height: 1000px;
    overflow: hidden;
    background: var(--page-bg);
  }
  .business-card {
    position: absolute;
    left: 100px;
    top: 211px;
    width: 1000px;
    height: 578px;
    background: var(--card-base);
    box-shadow: 0 14px 34px var(--shadow);
    overflow: hidden;
    font-family: "Alegreya Sans", sans-serif;
    color: var(--ink);
  }
  .swirl-pattern {
    position: absolute;
    inset: 0;
    background:
      radial-gradient(ellipse at 20% 30%, var(--card-swirl) 0%, transparent 45%),
      radial-gradient(ellipse at 80% 75%, var(--card-swirl) 0%, transparent 50%),
      linear-gradient(160deg, var(--card-base) 0%, var(--card-light) 55%, var(--card-base) 100%);
  }
  .brand {
    position: absolute;
    left: 80px;
    top: 200px;
    display: flex;
    align-items: center;
    gap: 22px;
  }
  .brand-mark {
    width: 34px;
    height: 34px;
    background: var(--ink);
  }
  .brand-name {
    font-size: 100px;
    font-weight: 500;
    line-height: 1;
    letter-spacing: 1px;
  }
  .contact-list {
    position: absolute;
    left: 560px;
    top: 210px;
    margin: 0;
    padding: 0;
    list-style: none;
    font-size: 27px;
    line-height: 1.2;
  }
  .contact-item {
    display: flex;
    align-items: flex-start;
    gap: 16px;
    margin-bottom: 22px;
  }
  .contact-icon {
    width: 26px;
    height: 30px;
    flex: none;
    fill: var(--ink);
  }
  .website {
    position: absolute;
    left: 560px;
    top: 440px;
    font-size: 27px;
  }
</style>
</head>
<body>
  <main class="business-card">
    <div class="swirl-pattern" role="img" aria-label="Soft golden swirl pattern background"></div>

    <div class="brand">
      <span class="brand-mark"></span>
      <span class="brand-name">Morvex</span>
    </div>

    <ul class="contact-list">
      <li class="contact-item">
        <svg class="contact-icon" viewBox="0 0 24 30" aria-hidden="true">
          <path d="M12 1C6.5 1 3 5 3 10c0 6.5 9 18 9 18s9-11.5 9-18c0-5-3.5-9-9-9zm0 13a4 4 0 1 1 0-8 4 4 0 0 1 0 8z"/>
        </svg>
        <span>214 Larkmere rd, elwood park,<br>3184</span>
      </li>
      <li class="contact-item">
        <svg class="contact-icon" viewBox="0 0 24 30" aria-hidden="true">
          <path d="M7 1h10a2 2 0 0 1 2 2v24a2 2 0 0 1-2 2H7a2 2 0 0 1-2-2V3a2 2 0 0 1 2-2zm0 3v19h10V4zm5 21a1.3 1.3 0 1 0 0 2.6 1.3 1.3 0 0 0 0-2.6z"/>
        </svg>
        <span>03 9184 2730</span>
      </li>
      <li class="contact-item">
        <svg class="contact-icon" viewBox="0 0 24 30" aria-hidden="true">
          <path d="M1 8h22v15H1zm2 2v.6l9 6 9-6V10zm0 3v8h18v-8l-9 6z"/>
        </svg>
        <span>Morvex214@mailbox.example</span>
      </li>
    </ul>

    <div class="website">www.morvex.example.au</div>
  </main>
</body>
</html>
```